Harbormile Trade Associates - Letterhead and Folder

I am looking for letterhead that uses the splash from the logo on the side of the page as well as some information from our website.

I am looking for a folder that is a fold out that has pockets to hold paper as well as a slits for a business card.

Website address is www.harbormiletradeassociates.example

Target Market(s)

Export of Agrifoods, commodities and emergency aid.
Supplying the world food security.

Requirements
Must have
• Use splash and logo, have information about company.
• Letterhead must have splash on a side not in the middle.
Nice to have
• Different pictures that what are provided.

```html
<!DOCTYPE html>
<html lang="en">
<head>
<meta charset="utf-8">
<title>Harbormile Trade Associates – Letterhead and Folder</title>
<link href="https://fonts.googleapis.com/css2?family=Cinzel:wght@700&family=Montserrat:wght@500;600&display=swap" rel="stylesheet">
<style>
  :root{
    --backdrop:#eeeff0;
    --paper:#ffffff;
    --navy:#3e6083;
    --ink:#1e1e1e;
    --green:#4da246;
    --splash:#d7e6c4;
    --shadow:0 4px 14px rgba(0,0,0,.28);
  }
  *{box-sizing:border-box;margin:0;padding:0}
  html,body{width:1200px;height:1200px;overflow:hidden}
  body{background:var(--backdrop);position:relative;font-family:"Montserrat",sans-serif}

  .sheet{position:absolute;background:var(--paper);box-shadow:var(--shadow);overflow:hidden}
  .brand{position:absolute;display:flex;align-items:center;gap:14px}
  .brand__dot{border-radius:50%;border:3px solid var(--green);flex:none}
  .brand__name{font-family:"Cinzel",serif;font-weight:700;color:var(--ink);line-height:1.05}
  .brand__name .line1{display:block}
  .brand__name .line2{display:flex;align-items:center;gap:6px;letter-spacing:.28em}
  .brand__name .line2::before,.brand__name .line2::after{content:"";flex:1;height:1px;background:var(--ink)}
  .rule{position:absolute;height:1.5px;background:var(--navy)}
  .splash{position:absolute;border-radius:50%;border:6px solid var(--splash);background:rgba(215,230,196,.35)}

  /* Letterhead */
  .letterhead{left:190px;top:34px;width:410px;height:580px}
  .letterhead .brand{left:36px;top:36px}
  .letterhead .brand__dot{width:62px;height:62px}
  .letterhead .brand__name{font-size:19px}
  .letterhead .brand__name .line2{font-size:11px}
  .letterhead .rule{left:30px;right:30px;top:122px}
  .letterhead .splash{width:150px;height:150px;right:-60px;top:350px}
  .letterhead .foot-rule{position:absolute;left:0;right:0;bottom:52px;height:2px;background:var(--navy)}
  .letterhead .address{position:absolute;right:14px;bottom:40px;font-size:6.5px;color:var(--navy);font-weight:500}
  .letterhead .band{position:absolute;left:0;right:0;bottom:0;height:34px;background:var(--navy);color:#fff;font-size:8px;font-weight:600;letter-spacing:.12em;display:flex;align-items:center;justify-content:flex-end;padding-right:14px}

  /* Folder cover */
  .cover{left:668px;top:26px;width:416px;height:584px;background:var(--navy)}
  .cover__ring{position:absolute;left:50%;top:168px;width:170px;height:170px;margin-left:-85px;border-radius:50%;border:8px solid #fff}
  .cover__name{position:absolute;left:0;right:0;top:350px;text-align:center;font-family:"Cinzel",serif;font-weight:700;color:#fff}
  .cover__name .line1{display:block;font-size:40px;letter-spacing:.01em}
  .cover__name .line2{display:flex;align-items:center;gap:10px;font-size:20px;letter-spacing:.28em;margin:4px 42px 0}
  .cover__name .line2::before,.cover__name .line2::after{content:"";flex:1;height:1.5px;background:#fff}
  .cover__web{position:absolute;left:0;right:0;bottom:26px;text-align:center;color:#fff;font-size:8px;font-weight:600;letter-spacing:.12em}

  /* Folder inside */
  .inside{left:284px;top:654px;width:726px;height:508px;background:var(--paper);box-shadow:var(--shadow)}
  .inside__fold{position:absolute;left:362px;top:0;bottom:0;width:1px;background:#e4e4e4}
  .inside__splash{position:absolute;left:320px;top:100px;width:170px;height:300px;border-radius:0 150px 150px 0;background:var(--splash);opacity:.8}
  .insert{position:absolute;background:var(--paper);box-shadow:0 1px 6px rgba(0,0,0,.22);overflow:hidden}
  .insert .brand__dot{width:52px;height:52px}
  .insert .brand__name{font-size:15px}
  .insert .brand__name .line2{font-size:9px}
  .insert--left{left:22px;top:32px;width:318px;height:400px}
  .insert--right{left:392px;top:40px;width:300px;height:400px}
  .insert .brand{left:26px;top:24px}
  .insert .rule{left:20px;right:12px;top:90px;height:1px}
  .insert .splash{width:100px;height:100px;right:-40px;top:250px;border-width:4px}
  .pocket{position:absolute;top:386px;bottom:0;background:var(--navy)}
  .pocket--left{left:0;width:358px;border-top-right-radius:14px}
  .pocket--right{left:368px;right:0;border-top-left-radius:14px}
</style>
</head>
<body>

<section class="sheet letterhead" aria-label="Letterhead">
  <div class="brand">
    <span class="brand__dot"></span>
    <div class="brand__name"><span class="line1">Harbormile Trade</span><span class="line2">Associates</span></div>
  </div>
  <div class="rule"></div>
  <div class="splash" role="img" aria-label="Faint brand splash at page edge"></div>
  <div class="foot-rule"></div>
  <p class="address">Harbormile Trade Associates Ltd. 410-220 Quay St. W. Portsmere, SK S0X1A0</p>
  <div class="band">www.harbormiletradeassociates.example</div>
</section>

<section class="sheet cover" aria-label="Folder cover">
  <div class="cover__ring"></div>
  <div class="cover__name"><span class="line1">Harbormile Trade</span><span class="line2">Associates</span></div>
  <p class="cover__web">www.harbormiletradeassociates.example</p>
</section>

<section class="sheet inside" aria-label="Folder inside with pockets">
  <div class="inside__fold"></div>
  <div class="inside__splash" role="img" aria-label="Large brand splash printed on inside panel"></div>

  <div class="insert insert--left">
    <div class="brand">
      <span class="brand__dot"></span>
      <div class="brand__name"><span class="line1">Harbormile Trade</span><span class="line2">Associates</span></div>
    </div>
    <div class="rule"></div>
    <div class="splash" role="img" aria-label="Faint brand splash"></div>
  </div>

  <div class="insert insert--right">
    <div class="brand">
      <span class="brand__dot"></span>
      <div class="brand__name"><span class="line1">Harbormile Trade</span><span class="line2">Associates</span></div>
    </div>
    <div class="rule"></div>
    <div class="splash" role="img" aria-label="Faint brand splash"></div>
  </div>

  <div class="pocket pocket--left"></div>
  <div class="pocket pocket--right"></div>
</section>

</body>
</html>
```